GREEK DELICATESSEN FRONT AND SIDE SIGNAGE

This Greek shop will include both a retail store and a small commercial kitchen for cooking demonstrations, small catering events etc. with each of these two functions having their own logos which are included in this project. These two logos are included both as pdf and psd format so you can slightly adjust the colors if needed to match the background which we would like to be a shade (or shades) of blue.
The shop has two sides as per the attached pictures where the front larger signage of 14.35m X 1.23m will include the wording: GREEK FOOD WINE AND MORE followed by the AMBER HARBOUR logo and after that we want to add the sentence AUTHENTIC HOME COOKING followed by the logo NORA'S GREEK KITCHEN. Somewhere on the signage we must include our website which is www.plumorchard.co.nz and our phone number which is 0800 MOLTAP.
The second side being being much smaller at 6.37m X 1.23m must only include the wording GREEK FOOD WINE AND MORE followed by the AMBER HARBOUR logo and all above contact details.

Target Market(s)

RETAIL CUSTOMERS AND FOOD LOVERS

Industry/Entity Type

Retail

Colors
33a6d7
3176b5
0492cd
0255a3
85cae6

Requirements
Nice to have
• SMALL GREEK FLAG
Should not have
• GREEK RUINS, SANTORINI PHOTOS

```html
<!DOCTYPE html>
<html lang="en">
<head>
<meta charset="utf-8">
<title>Amber Harbour – Shop Signage</title>
<link rel="stylesheet" href="https://fonts.googleapis.com/css2?family=Exo+2:wght@500;600&family=Open+Sans:wght@400;600&display=swap">
<style>
  :root {
    --sign-blue: #1f80c5;
    --panel-navy: #0a4c94;
    --panel-glow: #1e6cb8;
    --ink-white: #ffffff;
    --olive-lime: #c9d93a;
    --flag-blue: #0d6fc0;
    --page: #ffffff;
  }
  * { margin: 0; padding: 0; box-sizing: border-box; }
  html, body { width: 1200px; height: 355px; overflow: hidden; background: var(--page); }
  .canvas { position: relative; width: 1200px; height: 355px; }

  .sign { position: absolute; background: var(--sign-blue); color: var(--ink-white); overflow: hidden; }
  .sign--front { left: 41px; top: 59px; width: 1111px; height: 95px; }
  .sign--side  { left: 350px; top: 209px; width: 493px; height: 95px; }

  .abs { position: absolute; }

  .brand { display: flex; align-items: center; gap: 6px; font-family: "Exo 2", sans-serif; font-weight: 600; color: var(--olive-lime); white-space: nowrap; }
  .brand__dot { width: 12px; height: 12px; border-radius: 50%; background: var(--olive-lime); flex: none; }
  .sign--front .brand { left: 18px; top: 38px; font-size: 17px; letter-spacing: 0.4px; }
  .sign--side .brand { left: 20px; top: 38px; font-size: 14px; letter-spacing: 0.3px; }

  .flag { left: 215px; top: 20px; width: 62px; height: 42px; }

  .headline { font-family: "Exo 2", sans-serif; font-weight: 600; line-height: 1; white-space: nowrap; }
  .sign--front .headline { left: 296px; top: 16px; font-size: 50px; letter-spacing: 1.5px; }
  .sign--side .headline { left: 186px; top: 12px; font-size: 32px; letter-spacing: 0; }

  .tagline { font-family: "Exo 2", sans-serif; font-weight: 500; white-space: nowrap; line-height: 1; }
  .sign--front .tagline { left: 464px; top: 68px; font-size: 17px; letter-spacing: 6px; }
  .sign--side .tagline { left: 186px; top: 50px; width: 262px; font-size: 11px; letter-spacing: 2.6px; display: flex; align-items: center; justify-content: center; gap: 10px; }
  .tagline__rule { width: 55px; height: 1px; background: var(--ink-white); }

  .kitchen { left: 752px; top: 22px; width: 50px; font-family: "Exo 2", sans-serif; font-weight: 600; font-size: 8px; line-height: 1.15; text-align: center; }
  .kitchen__host { left: 752px; top: 57px; width: 50px; text-align: center; font-family: "Exo 2", sans-serif; font-weight: 500; font-size: 10px; letter-spacing: 0.3px; }
  .promise { left: 807px; top: 30px; font-family: "Exo 2", sans-serif; font-weight: 600; font-size: 16px; line-height: 20px; letter-spacing: 0.3px; }

  .contact-panel { right: 0; top: 0; width: 157px; height: 95px; background: var(--panel-navy); }
  .contact-panel__glow { right: 0; top: 0; width: 120px; height: 95px; background: radial-gradient(circle at 80% 50%, var(--panel-glow) 0%, rgba(30,108,184,0) 70%); }
  .side-glow { left: 0; top: 0; width: 170px; height: 95px; background: radial-gradient(circle at 30% 70%, #3a93d2 0%, rgba(58,147,210,0) 70%); }

  .contact { display: flex; align-items: center; gap: 8px; white-space: nowrap; }
  .contact svg { width: 11px; height: 11px; flex: none; }
  .contact--web { font-family: "Open Sans", sans-serif; font-size: 9.5px; }
  .contact--phone { font-family: "Exo 2", sans-serif; font-weight: 600; font-size: 16px; letter-spacing: 0.5px; }
  .contact-panel .contact--web { left: 14px; top: 30px; }
  .contact-panel .contact--phone { left: 14px; top: 44px; }
  .sign--side .contact--web { left: 186px; top: 71px; }
  .sign--side .contact--phone { left: 332px; top: 68px; }
</style>
</head>
<body>
<div class="canvas">

  <section class="sign sign--front" aria-label="Front signage">
    <div class="abs brand"><span class="brand__dot"></span>AMBER HARBOUR</div>

    <svg class="abs flag" viewBox="0 0 27 18" role="img" aria-label="Greek flag">
      <rect width="27" height="18" fill="#ffffff"/>
      <g fill="var(--flag-blue)">
        <rect y="0" width="27" height="2"/>
        <rect y="4" width="27" height="2"/>
        <rect y="8" width="27" height="2"/>
        <rect y="12" width="27" height="2"/>
        <rect y="16" width="27" height="2"/>
        <rect width="10" height="10"/>
      </g>
      <rect x="4" y="0" width="2" height="10" fill="#ffffff"/>
      <rect x="0" y="4" width="10" height="2" fill="#ffffff"/>
    </svg>

    <div class="abs headline">GREEK FOOD WINE</div>
    <div class="abs tagline">AND MORE</div>

    <div class="abs kitchen">NORA'S GREEK KITCHEN</div>
    <div class="abs kitchen__host">HOSTING</div>
    <div class="abs promise">AUTHENTIC<br>HOME COOKING</div>

    <div class="abs contact-panel">
      <div class="abs contact-panel__glow" role="img" aria-label="Soft dotted halftone texture"></div>
      <div class="abs contact contact--web">
        <svg viewBox="0 0 12 12" fill="none" stroke="#fff" stroke-width="1"><circle cx="6" cy="6" r="5"/><ellipse cx="6" cy="6" rx="2.2" ry="5"/><path d="M1 6h10M2 3.3h8M2 8.7h8"/></svg>
        www.plumorchard.co.nz
      </div>
      <div class="abs contact contact--phone">
        <svg viewBox="0 0 12 12" fill="#fff"><path d="M2.6 1.2l1.7 1.7-1 1.3c.6 1.5 1.7 2.6 3.2 3.3l1.3-1 1.8 1.7-1.1 1.7C5.5 9.8 2.2 6.5 1.2 3z"/><path d="M7 1.3a4 4 0 0 1 3.7 3.7" stroke="#fff" fill="none" stroke-width=".9"/></svg>
        0800 MOLTAP
      </div>
    </div>
  </section>

  <section class="sign sign--side" aria-label="Side signage">
    <div class="abs side-glow" role="img" aria-label="Soft dotted halftone texture"></div>
    <div class="abs brand"><span class="brand__dot"></span>AMBER HARBOUR</div>
    <div class="abs headline">GREEK FOOD WINE</div>
    <div class="abs tagline"><span class="tagline__rule"></span>AND MORE<span class="tagline__rule"></span></div>
    <div class="abs contact contact--web">
      <svg viewBox="0 0 12 12" fill="none" stroke="#fff" stroke-width="1"><circle cx="6" cy="6" r="5"/><ellipse cx="6" cy="6" rx="2.2" ry="5"/><path d="M1 6h10M2 3.3h8M2 8.7h8"/></svg>
      www.plumorchard.co.nz
    </div>
    <div class="abs contact contact--phone">
      <svg viewBox="0 0 12 12" fill="#fff"><path d="M2.6 1.2l1.7 1.7-1 1.3c.6 1.5 1.7 2.6 3.2 3.3l1.3-1 1.8 1.7-1.1 1.7C5.5 9.8 2.2 6.5 1.2 3z"/><path d="M7 1.3a4 4 0 0 1 3.7 3.7" stroke="#fff" fill="none" stroke-width=".9"/></svg>
      0800 MOLTAP
    </div>
  </section>

</div>
</body>
</html>
```